Silver Creek Plumbing Business card & letter head design

We need a new business card and letter head for our plumbing company called silver creek plumbing. attached is the companys logo. We provide domestic and commercial plumbing services in regional western Australia. We are after Something simple yet nice to look at and something that fits within the trade industry.

Target Market(s)

trade/building industry

Contact Information for Business Card

Darl Hensby
Manager
0461 238 574
enquiries@scplumbwork.net.au
ABN: 47 381 905 462
PCL: 5187

Domestic & Commercial Plumbing
Tip Truck & Excavator hire

Colors

Designer to choose colors to be used in the design.

```html
<!DOCTYPE html>
<html lang="en">
<head>
<meta charset="UTF-8">
<title>Silver Creek Plumbing – Business Card</title>
<link rel="stylesheet" href="https://fonts.googleapis.com/css2?family=Montserrat:wght@700;800&family=Lato:ital,wght@0,400;0,700;1,400&display=swap">
<style>
  :root {
    --brand-blue: #1459a8;
    --ink-blue: #1a4fa0;
    --ink-grey: #3a3a3a;
    --paper: #ffffff;
    --backdrop: #e6e7ea;
  }
  * { margin: 0; padding: 0; box-sizing: border-box; }
  html, body { width: 1200px; height: 878px; overflow: hidden; }
  body {
    background: var(--backdrop);
    font-family: "Lato", sans-serif;
    display: flex;
    flex-direction: column;
    align-items: center;
    justify-content: center;
    gap: 26px;
  }
  .card {
    width: 700px;
    height: 400px;
    position: relative;
    box-shadow: 0 6px 18px rgba(0,0,0,0.18);
  }
  .card--back {
    background: var(--brand-blue);
    display: flex;
    align-items: center;
    justify-content: center;
  }
  .wordmark {
    font-family: "Montserrat", sans-serif;
    font-weight: 800;
    text-transform: uppercase;
    letter-spacing: 0.5px;
    line-height: 1.05;
    display: flex;
    align-items: center;
    gap: 14px;
  }
  .wordmark__dot {
    width: 22px; height: 22px; border-radius: 50%;
    flex: none;
  }
  .card--back .wordmark { color: var(--paper); font-size: 40px; }
  .card--back .wordmark__dot { background: var(--paper); }

  .card--front { background: var(--paper); }
  .card--front .wordmark {
    position: absolute; left: 56px; top: 58px;
    color: var(--ink-blue); font-size: 28px;
  }
  .card--front .wordmark__dot { background: var(--ink-blue); width: 18px; height: 18px; }

  .holder {
    position: absolute; right: 56px; top: 112px; text-align: right;
  }
  .holder__name {
    font-family: "Montserrat", sans-serif; font-weight: 800;
    font-size: 32px; color: var(--ink-blue); text-transform: uppercase;
  }
  .holder__role { font-size: 19px; color: var(--ink-grey); margin-top: 2px; }

  .divider {
    position: absolute; left: 56px; right: 56px; top: 228px;
    height: 2px; background: var(--ink-blue);
  }

  .contacts {
    position: absolute; left: 56px; bottom: 34px;
    list-style: none; font-size: 18px; color: var(--ink-grey);
    font-style: italic; line-height: 1.6;
  }
  .contacts li { display: flex; align-items: center; gap: 9px; }
  .contacts svg { width: 16px; height: 16px; fill: var(--ink-blue); flex: none; }
  .contacts .label { color: var(--ink-blue); font-style: normal; }

  .services {
    position: absolute; right: 56px; bottom: 40px;
    text-align: right; font-size: 18px; color: var(--ink-grey); line-height: 1.45;
  }
</style>
</head>
<body>
  <section class="card card--back" aria-label="Card back">
    <div class="wordmark"><span class="wordmark__dot"></span>Silver Creek Plumbing</div>
  </section>

  <section class="card card--front" aria-label="Card front">
    <div class="wordmark"><span class="wordmark__dot"></span>Silver Creek Plumbing</div>

    <div class="holder">
      <div class="holder__name">Darl Hensby</div>
      <div class="holder__role">Manager</div>
    </div>

    <div class="divider"></div>

    <ul class="contacts">
      <li>
        <svg viewBox="0 0 24 24" aria-hidden="true"><path d="M6.6 10.8a15.1 15.1 0 0 0 6.6 6.6l2.2-2.2c.3-.3.7-.4 1-.2 1.1.4 2.3.6 3.6.6.6 0 1 .4 1 1V20c0 .6-.4 1-1 1A17 17 0 0 1 3 4c0-.6.4-1 1-1h3.5c.6 0 1 .4 1 1 0 1.3.2 2.5.6 3.6.1.3 0 .7-.2 1z"/></svg>
        0461 238 574
      </li>
      <li>
        <svg viewBox="0 0 24 24" aria-hidden="true"><path d="M2 5h20v14H2z M2 5l10 8 10-8" fill="none" stroke="#1a4fa0" stroke-width="2"/></svg>
        enquiries@scplumbwork.net.au
      </li>
      <li><span class="label">ABN:</span> 47 381 905 462</li>
      <li><span class="label">PCL:</span> 5187</li>
    </ul>

    <div class="services">
      Domestic &amp; Commercial Plumbing<br>
      Tip Truck &amp; Excavator hire
    </div>
  </section>
</body>
</html>
```